Stationery Design
Letterhead, Envelope, Business Card, Email signature design
I need single sided standard sized Business Card [3.5" x 2"]
Myriad Pro
Professional
Corisse Pallant
Brand Manager
4127 Dunford Avenue
Burnaby, B.C. V3K 8T2
604-281-7734 ext. 120
corisse@brightfernco.ca
brightfernco.ca
We are a family-owned school photography company in Western Canada. We've just had a new logo and website designed and need some new stationery.
This is the .ai file we would like to use for the stationery design. Please refer to our website, brightfernco.ca, for more information about our brand.

```html
<!DOCTYPE html>
<html lang="en">
<head>
<meta charset="utf-8">
<title>Bright Fern Co — Business Card</title>
<link href="https://fonts.googleapis.com/css2?family=Source+Sans+3:ital,wght@0,400;0,600;0,700;1,400;1,600;1,700&display=swap" rel="stylesheet">
<style>
  :root {
    --page-bg: #3a3b3d;
    --card-white: #ffffff;
    --brand-blue: #1f9ec4;
    --slate: #5d6066;
    --text-grey: #6b6e73;
    --rule: #d7dadd;
    --faint: rgba(255, 255, 255, 0.28);
  }
  * { margin: 0; padding: 0; box-sizing: border-box; }
  html, body {
    width: 1200px; height: 852px; overflow: hidden;
    background: var(--page-bg);
    font-family: "Source Sans 3", sans-serif;
  }
  .stage { position: relative; width: 1200px; height: 852px; }
  .card {
    position: absolute; width: 560px; height: 320px;
    border-radius: 16px; overflow: hidden;
  }
  .card-front { left: 80px; top: 110px; background: var(--card-white); }
  .card-back { left: 560px; top: 430px; background: var(--brand-blue); }

  .front-curves { position: absolute; inset: 0; width: 560px; height: 320px; overflow: hidden; }

  .wordmark { position: absolute; left: 34px; top: 34px; display: flex; align-items: center; gap: 10px; }
  .wordmark-square { width: 30px; height: 30px; background: var(--brand-blue); }
  .wordmark-name {
    font-size: 30px; font-weight: 700; color: var(--brand-blue);
    letter-spacing: -0.5px; line-height: 1;
  }

  .person { position: absolute; left: 34px; top: 118px; font-size: 17px; }
  .person-name { color: var(--brand-blue); font-weight: 700; font-style: italic; }
  .person-role { color: var(--text-grey); font-weight: 600; font-style: italic; font-size: 14px; }
  .person-rule { position: absolute; left: 34px; top: 144px; width: 330px; height: 1px; background: var(--rule); }

  .contacts {
    position: absolute; left: 34px; top: 154px;
    display: grid; grid-template-columns: 150px 190px; row-gap: 7px; column-gap: 8px;
    font-size: 13px; color: var(--text-grey);
  }
  .contact { display: flex; align-items: center; gap: 6px; white-space: nowrap; }
  .contact svg { width: 12px; height: 12px; flex: none; }
  .contact-label { color: var(--brand-blue); font-weight: 600; }

  .address {
    position: absolute; left: 34px; top: 262px;
    font-size: 13px; color: var(--text-grey);
  }

  .back-disc {
    position: absolute; left: 50%; top: 50%;
    width: 210px; height: 210px; margin: -105px 0 0 -105px;
    border-radius: 50%; background: var(--faint);
  }
  .back-url {
    position: absolute; left: 0; right: 0; top: 50%; transform: translateY(-50%);
    text-align: center; color: var(--card-white);
    font-size: 17px; font-weight: 600; letter-spacing: 0.3px;
  }
</style>
</head>
<body>
<main class="stage">

  <section class="card card-front" aria-label="Business card front">
    <svg class="front-curves" viewBox="0 0 560 320" aria-hidden="true">
      <path d="M320 0 H560 V245 C525 135 445 45 320 0 Z" fill="var(--brand-blue)"/>
      <path d="M450 32 C515 95 548 180 560 250 V320 H535 C530 215 505 115 450 32 Z" fill="var(--slate)"/>
      <path d="M288 0 C405 28 505 115 560 228" fill="none" stroke="var(--brand-blue)" stroke-width="2"/>
    </svg>

    <div class="wordmark">
      <span class="wordmark-square"></span>
      <span class="wordmark-name">BRIGHTFERN CO</span>
    </div>

    <p class="person"><span class="person-name">Corisse Pallant</span> <span class="person-role">/ Brand Manager</span></p>
    <div class="person-rule"></div>

    <div class="contacts">
      <div class="contact">
        <svg viewBox="0 0 12 12"><path d="M3 1 L5 3.5 L4 5 C5 7 6 8 7.5 8.5 L9 7.5 L11 9.5 L9.5 11 C5 10.5 1.5 7 1 2.5 Z" fill="var(--brand-blue)"/></svg>
        <span><span class="contact-label">(T)</span> 1-888-520-3917</span>
      </div>
      <div class="contact">
        <svg viewBox="0 0 12 12"><path d="M3 1 L5 3.5 L4 5 C5 7 6 8 7.5 8.5 L9 7.5 L11 9.5 L9.5 11 C5 10.5 1.5 7 1 2.5 Z" fill="var(--brand-blue)"/></svg>
        <span>604-281-7734 ext. 120</span>
      </div>
      <div class="contact">
        <svg viewBox="0 0 12 12"><rect x="3.5" y="1" width="5" height="10" rx="1" fill="var(--brand-blue)"/></svg>
        <span>604-772-4068</span>
      </div>
      <div class="contact">
        <svg viewBox="0 0 12 12"><rect x="1" y="4" width="10" height="6" rx="1" fill="var(--brand-blue)"/><rect x="3" y="1" width="6" height="3" fill="var(--brand-blue)"/></svg>
        <span>604-281-7790</span>
      </div>
      <div class="contact">
        <svg viewBox="0 0 12 12"><rect x="1" y="2.5" width="10" height="7" rx="1" fill="var(--brand-blue)"/><path d="M1.5 3 L6 6.5 L10.5 3" stroke="#fff" fill="none"/></svg>
        <span>corisse@brightfernco.ca</span>
      </div>
      <div class="contact">
        <svg viewBox="0 0 12 12"><circle cx="6" cy="6" r="5" fill="var(--brand-blue)"/><path d="M1 6 H11 M6 1 C3.5 4 3.5 8 6 11 M6 1 C8.5 4 8.5 8 6 11" stroke="#fff" stroke-width="0.8" fill="none"/></svg>
        <span>www.brightfernco.ca</span>
      </div>
    </div>

    <p class="address">4127 Dunford Avenue Burnaby, B.C V3K 8T2</p>
  </section>

  <section class="card card-back" aria-label="Business card back">
    <div class="back-disc"></div>
    <p class="back-url">www.brightfernco.ca</p>
  </section>

</main>
</body>
</html>
```